Lionel's UPDATE -Across the Board

Insurance Agent Business card and probably everything else !
Been in business for over 35 years and never took the time to update so really like the black-gold combo but open for suggestions (Honestly, I have NO idea how this works but sounds very cool ) Attached are two samples that I enjoy. The black and gold option is my favorite so looking for something like that!

```html
<!DOCTYPE html>
<html lang="en">
<head>
<meta charset="utf-8">
<title>Lionel S Marsh – Business Card</title>
<link href="https://fonts.googleapis.com/css2?family=Tinos:wght@400;700&display=swap" rel="stylesheet">
<style>
  :root {
    --bg: #c9c9c7;
    --ink: #1d1d1b;
    --ink-soft: #2b2b29;
    --gold: #d8b96f;
    --gold-light: #ecd594;
    --gold-deep: #b8944a;
  }
  * { margin: 0; padding: 0; box-sizing: border-box; }
  html, body { width: 1200px; height: 675px; overflow: hidden; }
  body {
    background: var(--bg);
    font-family: "Tinos", "Times New Roman", serif;
    position: relative;
  }
  .card {
    position: absolute;
    top: 187px;
    width: 525px;
    height: 300px;
    border-radius: 18px;
    overflow: hidden;
    box-shadow: 0 10px 24px rgba(0,0,0,.28);
    background: var(--ink);
  }
  .card--back { left: 50px; }
  .card--front { left: 625px; }
  .card svg.art { position: absolute; inset: 0; }

  .monogram {
    position: absolute;
    color: var(--gold);
    font-size: 30px;
    font-weight: 400;
    letter-spacing: 2px;
    display: flex;
    align-items: center;
    gap: 10px;
    white-space: nowrap;
  }
  .monogram .dot {
    width: 10px; height: 10px;
    border-radius: 50%;
    background: var(--gold);
  }
  .card--back .monogram { left: 285px; top: 130px; }
  .card--front .monogram { left: 225px; top: 228px; font-size: 24px; }

  .identity {
    position: absolute;
    right: 26px;
    top: 62px;
    text-align: right;
    color: var(--ink);
    white-space: nowrap;
  }
  .identity .name { font-size: 28px; font-weight: 700; line-height: 1; }
  .identity .role { font-size: 12px; margin-top: 5px; }
  .identity .est { font-size: 10px; margin-top: 3px; }

  .contact {
    position: absolute;
    left: 26px;
    top: 34px;
    color: var(--gold);
    font-size: 13px;
    line-height: 1.35;
    list-style: none;
  }
  .contact li { display: flex; gap: 9px; margin-bottom: 8px; }
  .contact svg { width: 14px; height: 14px; flex: none; margin-top: 2px; }
</style>
</head>
<body>

<section class="card card--back" aria-label="Card back">
  <svg class="art" viewBox="0 0 525 300" aria-hidden="true">
    <defs>
      <linearGradient id="goldBack" x1="0" y1="0" x2="1" y2="1">
        <stop offset="0" stop-color="#d2b060"/>
        <stop offset=".5" stop-color="#ecd594"/>
        <stop offset="1" stop-color="#d3b267"/>
      </linearGradient>
    </defs>
    <path d="M0 168 C150 172 300 215 420 255 C470 272 505 282 525 274 L525 300 L0 300 Z" fill="url(#goldBack)"/>
    <path d="M0 178 C150 182 300 225 420 263 C470 279 505 288 525 282" fill="none" stroke="#1d1d1b" stroke-width="6"/>
    <path d="M0 190 C150 196 290 238 410 275 C460 290 500 296 525 292" fill="none" stroke="#1d1d1b" stroke-width="4"/>
  </svg>
  <div class="monogram"><span class="dot"></span>LSM</div>
</section>

<section class="card card--front" aria-label="Card front">
  <svg class="art" viewBox="0 0 525 300" aria-hidden="true">
    <defs>
      <linearGradient id="goldFront" x1="0" y1="0" x2="1" y2="1">
        <stop offset="0" stop-color="#ecd594"/>
        <stop offset=".6" stop-color="#d8b96f"/>
        <stop offset="1" stop-color="#c9a659"/>
      </linearGradient>
    </defs>
    <path d="M215 0 C240 60 235 130 300 190 C350 236 420 270 470 300 L525 300 L525 0 Z" fill="url(#goldFront)"/>
    <path d="M231 0 C256 60 251 130 316 190 C366 236 436 270 486 300" fill="none" stroke="#1d1d1b" stroke-width="6"/>
    <path d="M246 0 C271 60 266 130 331 190 C381 236 451 270 501 300" fill="none" stroke="#1d1d1b" stroke-width="3"/>
  </svg>

  <ul class="contact">
    <li>
      <svg viewBox="0 0 14 14"><path d="M7 1a4.5 4.5 0 0 0-4.5 4.5C2.5 9 7 13 7 13s4.5-4 4.5-7.5A4.5 4.5 0 0 0 7 1zm0 6.2a1.7 1.7 0 1 1 0-3.4 1.7 1.7 0 0 1 0 3.4z" fill="#d8b96f"/></svg>
      <span>1200 Harbor Way,<br>Suite 210-B,<br>Coral Grove,<br>FL 33000</span>
    </li>
    <li>
      <svg viewBox="0 0 14 14"><rect x="1" y="3" width="12" height="8" rx="1" fill="none" stroke="#d8b96f" stroke-width="1.4"/><path d="M1.5 3.5 7 8l5.5-4.5" fill="none" stroke="#d8b96f" stroke-width="1.4"/></svg>
      <span>lionel@lsmcover.com</span>
    </li>
    <li>
      <svg viewBox="0 0 14 14"><path d="M3 1.5h2.2l1 3-1.4 1a7 7 0 0 0 3.7 3.7l1-1.4 3 1v2.2A1.5 1.5 0 0 1 11 12.5 9.5 9.5 0 0 1 1.5 3 1.5 1.5 0 0 1 3 1.5z" fill="#d8b96f"/></svg>
      <span>Phone : 555-014-2237<br>Fax : 555-014-2290</span>
    </li>
  </ul>

  <div class="identity">
    <p class="name">Lionel S Marsh</p>
    <p class="role">Insurance &amp; Financial Consultant</p>
    <p class="est">Est. 1985</p>
  </div>

  <div class="monogram"><span class="dot"></span>LSM</div>
</section>

</body>
</html>
```